Design a Brochure for selling PCB pooling services

Our company manufactures printed circuits board (PCBs) used in the electronics industry. We need to make a one A4 page brochure (single or double sided) that explains the services offered, the steps to make the order and the price list. The attachment is a draft of the text that can be used in the brochure.
We will need to have the source files made in corel draw so we can make future modifications if needed.

```html
<!DOCTYPE html>
<html lang="en">
<head>
<meta charset="utf-8">
<title>Delta Circuit Works – PCB Pool Service</title>
<link rel="stylesheet" href="https://fonts.googleapis.com/css2?family=Signika:wght@600&family=Open+Sans:wght@400&family=Arimo:wght@400;700&display=swap">
<style>
:root{
  --navy:#1d4e9a;
  --heading:#1b3f7a;
  --hero-deep:#0f3a86;
  --hero-light:#4a8fe0;
  --col-left:#e6e7e9;
  --col-right:#d1d3d4;
  --text:#3a3a3a;
  --intro:#1f4a8c;
  --accent:#e0302b;
  --white:#ffffff;
}
*{margin:0;padding:0;box-sizing:border-box}
html,body{width:854px;height:1200px;overflow:hidden;background:var(--white)}
.brochure{position:relative;width:854px;height:1200px;overflow:hidden;background:var(--white);font-family:"Open Sans",sans-serif;color:var(--text)}
.hero{position:absolute;left:0;top:0;width:854px;height:193px}
.hero-art{position:absolute;inset:0;background:linear-gradient(100deg,#0b2f78 0%,var(--hero-light) 45%,#a9cdf5 75%,var(--hero-deep) 100%)}
.hero-panel{position:absolute;left:0;top:0}
.brand{position:absolute;left:34px;top:40px;width:200px;font-family:"Signika",sans-serif;font-weight:600;font-size:27px;line-height:30px;color:var(--white);letter-spacing:.5px}
.column{position:absolute;top:225px;height:975px}
.column-left{left:4px;width:423px;background:var(--col-left)}
.column-right{left:427px;width:423px;background:var(--col-right)}
.intro{position:absolute;left:34px;top:238px;width:784px;height:82px;background:var(--white);border-radius:16px;padding:12px 16px;font-family:"Arimo",sans-serif;font-size:14.2px;line-height:19px;color:var(--intro);text-align:right}
.section{position:absolute}
.section h2{font-family:"Signika",sans-serif;font-weight:600;font-size:15.5px;color:var(--heading);display:flex;align-items:center;gap:8px;margin-left:-40px;height:20px}
.section h2::before{content:"";width:28px;height:14px;border-radius:7px;background:var(--navy);flex:none}
.section .body{border-left:1px solid #b5b7ba;padding-left:4px;margin-top:2px;font-size:10.9px;line-height:14px;text-align:justify}
.section ul{list-style:none}
.section li{position:relative;padding-left:19px;text-align:left}
.section li::before{content:"•";position:absolute;left:2px}
.cta{position:absolute;left:460px;top:693px;width:360px;text-align:center;font-family:"Arimo",sans-serif;font-size:18px;line-height:24px;color:var(--accent)}
.cta strong{font-size:21px}
.table-space,.contact-space{position:absolute;background:var(--white);border-radius:24px;display:flex;align-items:center;justify-content:center;text-align:center;font-family:"Arimo",sans-serif;color:#2a2a2a}
.table-space{left:155px;top:814px;width:568px;height:248px;font-size:34px}
.contact-space{left:44px;top:1097px;width:354px;height:84px;font-size:31px;line-height:38px}
</style>
</head>
<body>
<main class="brochure">
  <header class="hero">
    <div class="hero-art" role="img" aria-label="Blue close-up of printed circuit board traces"></div>
    <svg class="hero-panel" width="330" height="150" viewBox="0 0 330 150">
      <polygon points="0,0 322,0 258,146 0,146" fill="#1d4e9a"/>
      <polyline points="322,0 258,146 0,146" fill="none" stroke="#ffffff" stroke-width="3"/>
    </svg>
    <div class="brand">DELTA CIRCUIT WORKS</div>
  </header>

  <div class="column column-left"></div>
  <div class="column column-right"></div>

  <p class="intro">Our PCB pool service offers you the most cost effective solution to maximize your profit of your product. We specialize in arraying several numbers of PCBs with different designs to maximize cost and improve productivity. We maximize a wide range of PCB design, come to us and get a cost-effective panel design!</p>

  <section class="section" style="left:50px;top:342px;width:362px">
    <h2>QUALITY ASSURANCE</h2>
    <div class="body">Quality of service and the product should never be in question. Here in our company, we actually don't need to discuss about quality, as it is inherent in our minds that we only produce in accordance to IPC standards class 2 and none lesser than that.</div>
  </section>

  <section class="section" style="left:50px;top:452px;width:362px">
    <h2>WHY WE DO IT?</h2>
    <div class="body">We have a vision of creating a partnership with our customers. We don't regard our customers as the way to earn profits but as help in fulfilling each other's business objectives. We do mixed model PCB pooling because we want our customer partners to achieve the best manufacturability and profitability as possible as it can be. We do it for the best of both parties and we do it well.</div>
  </section>

  <section class="section" style="left:50px;top:593px;width:362px">
    <h2>STEPS DO GET YOUR PCB</h2>
    <div class="body">Below are the simple steps in getting your PCB from us:
      <ul>
        <li>Sign up now on our website (insert website here) and create your account.</li>
        <li>Fill-up the necessary items on the concise drop down menus</li>
        <li>Attach files on the “Attachments” action button if you have items that could help us in providing you the most optimum pricing</li>
        <li>Click the “Order” button</li>
        <li>Sit back and relax, you'll get your PCB the soonest possible time</li>
      </ul>
    </div>
  </section>

  <section class="section" style="left:480px;top:345px;width:352px">
    <h2>SPEED AND LEAD TIME</h2>
    <div class="body">Our manufacturing lines are flexible for all your manufacturing requirements. We have a wide range of price options for every manufacturing lead time that you require. We are flexible and adaptable to your needs and have special packages for quick turnover projects.</div>
  </section>

  <section class="section" style="left:480px;top:467px;width:352px">
    <h2>HOW WE DO IT?</h2>
    <div class="body">We have state of the art PCB designing tools that perform right through your needs. Our modelling tools can provide you the best cost in accordance to your submitted requirements.<br>We provide a wide range of specification capabilities that suits your needs such as:
      <ul>
        <li>Micro via sizes from 100 um to 4 mils</li>
        <li>Layer number of up to 16.</li>
        <li>Complete finish with up to 2 solder masks and silk screens</li>
        <li>Full ROHS compliant raw materials</li>
        <li>100% inspection for manufacturability and electrical</li>
      </ul>
    </div>
  </section>

  <p class="cta">Contact us now and get a <strong>free</strong> estimate of your PCB pooling requirement!</p>

  <div class="table-space">Table Space</div>
  <div class="contact-space">contac details<br>space</div>
</main>
</body>
</html>
```